EXCITING DECK for Automotive dealers that shows how our Technology works.

General Concept
The deck should visually represent the Trade and Credit Lead Life Cycle program is a dynamic, interconnected journey, illustrating how leads are generated, nurtured, and converted. The focus should be on how your system flows seamlessly between credit and trade-in opportunities for consumers, with the goal of maximizing engagement and conversions.
Slide 1: Title Slide - Lead Life Cycle Program
• Visual Concept: A stylized cycle or wheel that represents the stages of the lead life cycle, with arrows connecting each stage.
• Headline: "Lead Life Cycle Program"
• Subhead line: "Credit Pre-Qualification and Trade-In Appraisal"
• Imagery: Modern, sleek graphics of vehicles, smartphones (for texting), email icons, and dollar signs for value.
Slide 2: Lead Generation Sources
• Visual Concept: A funnel with the top representing the different lead generation sources.
• Content:
o Top of Funnel (Leads Enter):
 Pre-Qualification Tool (Swift4Loan)- How it Works
 1. Converts Web Traffic into the highest quality lead on the market
 Replyon Email/Mail Marketing – How it Works
 1. Delivers actionable leads from email marketing not Just OPENS AND CLICKS. Show the text demo. Audiences below
1. Past Sold Customers (Equity Targets)
2. Past Service Onlu Department Customers (Conquest Sales)
3. Unsold Leads (from previous interactions)
o Each source should have a distinct icon to represent it (e.g., envelope for email, a wrench for past service customers, etc.).
• Headline: "Multiple Lead Sources Feeding into the Program"
• Imagery: The funnel narrowing toward the next step with leads symbolized by icons flowing downward.
Slide 3: Credit Leads - Pre-Qualified Flow
• Visual Concept: A customer engaging with the Swift4Loan tool on their mobile, being pre-qualified, and then us sending a offer to appraise their trade.
• Flow Explanation:
o Customer pre-qualifies via Swift4Loan → Receives credit approval → Email and Mail Example to check trade-in value.
• Headline: "Pre-Qualified Leads: Offering Trade-In Appraisal"
• Imagery: A sequence that shows how a customer moves from pre-qualification to considering their trade-in value. To purchasing
Slide 4: Trade-In Leads - Valuation Flow
• Visual Concept: A customer who has received a trade-in valuation offer now being prompted to pre-qualify for financing.
• Flow Explanation:
o Customer texts for vehicle value → Receives trade-in appraisal → Offer to pre-qualify for financing appears link is at the bottom of the text response.
• Headline: "Trade-In Leads: Offering Credit Pre-Qualification"
• Imagery: A customer looking at their trade-in value on their phone and being shown an additional prompt to pre-qualify for a loan.
Slide 5: Cross-Offer Opportunities
• Visual Concept: A two-way street or cycle, illustrating the seamless transition between offering pre-qualification to trade-in customers and offering trade-in value to credit leads.
• Content:
o Two pathways:
1. Start as a Credit Lead → Offer Trade-In Valuation
2. Start as a Trade-In Lead → Offer Credit Pre-Qualification
o Headline: "Cross-Offer Opportunities for Maximum Engagement"
• Imagery: Arrows going in both directions, symbolizing the back-and-forth opportunities between credit and trade leads.
Digital Retargeting for Cross-Action Engagement
• Visual Concept: An omnichannel approach with a customer in the center, surrounded by email/Mail icons, Chatterly, and Snapvista logos. Arrows leading from each platform back to the customer, showing how these channels drive engagement.
• Content:
o Title: "Engage to Convert one lead type to get both with Email/Mail and Digital Retargeting"
o Explanation:
 Whether a lead starts as a Pre-Qualified Credit Lead or a Trade-In Valuation Lead, we use personalized Email/Mail Campaigns and Digital Retargeting Ads (Chatterly & Snapvista) to encourage them to take the next action.
 If they pre-qualify for credit, we retarget them with trade-in valuation offers.
 If they start with a trade-in valuation, we follow up with financing offers.
o Headline: "Leverage Email & Social Retargeting to Drive Cross-Action"
• Visuals:
o Icons of Email, Chatterly, and Snapvista: Showing the platforms through which you retarget leads.
o Customer Journey Map: Illustrating how leads who interacted once are guided to the next step (credit lead → trade-in offer, trade-in lead → pre-qualification).
o Arrows Flowing Between Channels: Showing how no matter where a lead starts, they are continually engaged through digital touchpoints until they complete both actions.
o Ad examples
• Call to Action: "Stay Top of Mind and Convert Leads into Multi-Action Customers"
This slide emphasizes how you’re leveraging both email/mail marketing and social media retargeting to move leads further along the customer journey, regardless of how they entered your funnel. The visuals should reinforce the idea of continuous engagement and omnipresent reminders for them to take action.
________________________________________
Slide 6: Lifecycle Representation
• Visual Concept: A circular diagram showing how leads can continuously move between credit and trade offers throughout their lifecycle.
• Content:
o Show how the lifecycle doesn’t end after one interaction, but can continue with follow-up offers.
o Headline: "Continuous Engagement Throughout the Lead Life Cycle"
• Imagery: Circular arrows or flowchart representing each stage looping back into the lifecycle, emphasizing that leads can be re-engaged.
Slide 7: Lead Conversion Goals
• Visual Concept: A progression from leads to successful transactions (e.g., a customer with keys to a new car). Showing that getting customers to take both of these actions delives a lead that is very committed to the process of buying.
• Content:
o End goal: Convert both credit and trade leads into sales.
o Show statistics or success metrics as optional data points.
o Headline: "Converting Leads into Sales"
• Imagery: A car dealership handing over keys, happy customers, and sold vehicles.
Slide 8: Next Steps / Call to Action
• Visual Concept: A final slide summarizing the key takeaways and next steps.
• Headline: "Maximize Lead Potential with Cross-Offer Opportunities"
• Imagery: A mix of credit leads, trade leads, and successful customer outcomes.
________________________________________These slides should be clean and modern, using simple but impactful visuals like arrows, icons, and flow diagrams to represent the journey. The key is to emphasize flow and interaction between credit and trade-in opportunities, showing the two-way cross-sell nature of your Lead Life Cycle Program.

I have attached a current deck so you can pull some basic product info and graphics into the new deck (PLEASE DONT JUST COPY THE OLD DECK). I have also included some of our email artwrok if you need it. If you want to look at our website go here www.kelmorvaleads.example

Target Market(s)

Car Dealers

Industry/Entity Type

Automotive Marketing

Requirements
Must have
• PLEASE READ THE PROJECT DESCRIPTION
Nice to have
Should not have
• PLEASE dont just copy the deck i uploaded. I am looking for a differnt take.

```html
<!DOCTYPE html>
<html lang="en">
<head>
<meta charset="utf-8">
<title>Kelmorva Marketing – Lead Life Cycle Deck</title>
<link href="https://fonts.googleapis.com/css2?family=Montserrat:wght@400;500;600;700&display=swap" rel="stylesheet">
<style>
:root{
  --board:#a9a9a9;
  --red:#e30613;
  --dark:#2f2f2f;
  --ink:#333333;
  --mid:#555555;
  --slide-bg:#f1f1f1;
  --white:#ffffff;
  --soft:#e4e4e4;
}
*{box-sizing:border-box;margin:0;padding:0}
html,body{width:1200px;height:528px;overflow:hidden;background:var(--board);font-family:'Montserrat',sans-serif}
.board{position:relative;width:1200px;height:528px}
.slide{position:absolute;width:720px;height:405px;transform:scale(0.4658);transform-origin:0 0;overflow:hidden;
  background:linear-gradient(120deg,#ececec 0%,#f7f7f7 35%,#eaeaea 36%,#f5f5f5 60%,#ededed 61%,#f8f8f8 100%)}
.slide .rule{position:absolute;left:39px;top:31px;width:154px;height:3px;background:linear-gradient(90deg,var(--red) 0 48%,var(--dark) 48% 100%)}
.slide .title{position:absolute;left:37px;top:54px;font-size:25px;font-weight:600;color:var(--red);line-height:1.08}
.slide .subtitle{position:absolute;left:39px;top:85px;font-size:16px;font-weight:500;color:var(--ink)}
.brand{position:absolute;left:548px;top:20px;width:142px;text-align:center;color:var(--dark);font-weight:600;font-size:15px;line-height:1.25;letter-spacing:3px}
.footer{position:absolute;left:0;bottom:0;width:720px;height:26px;background:var(--dark);color:var(--white);font-size:11.5px}
.footer .copy{position:absolute;left:39px;top:6px}
.footer .red{position:absolute;right:0;top:0;width:180px;height:26px;background:var(--red);clip-path:polygon(18px 0,100% 0,100% 100%,0 100%)}
.footer .bar{position:absolute;right:176px;top:0;width:12px;height:26px;background:var(--white);clip-path:polygon(8px 0,12px 0,4px 100%,0 100%)}
.footer .page{position:absolute;right:36px;top:6px}
.abs{position:absolute}
.photo{position:absolute}
.label{position:absolute;font-size:11px;color:var(--ink);text-align:center;line-height:1.4}
.card{position:absolute;top:100px;width:194px;height:232px;background:var(--white);box-shadow:0 2px 8px rgba(0,0,0,.12);text-align:center}
.card h3{margin-top:16px;font-size:10.5px;font-weight:500;color:var(--ink);line-height:1.7}
.card h3 em{font-style:normal;color:var(--red)}
.tiny{font-size:8px;color:var(--ink)}
</style>
</head>
<body>
<main class="board">

<!-- Slide 01 -->
<section class="slide" style="left:45px;top:54px">
  <div class="rule"></div>
  <h1 class="title">Lead Life Cycle</h1>
  <p class="subtitle">Trade Ready Credit Leads</p>
  <div class="brand">KELMORVA<br>MARKETING</div>
  <svg class="abs" style="left:410px;top:95px" width="280" height="265" viewBox="0 0 280 265">
    <circle cx="138" cy="132" r="122" fill="none" stroke="var(--dark)" stroke-width="11"/>
    <circle cx="138" cy="132" r="104" fill="var(--white)" stroke="var(--red)" stroke-width="3"/>
    <g fill="var(--white)" style="filter:drop-shadow(0 2px 4px rgba(0,0,0,.2))">
      <circle cx="43" cy="67" r="32"/><circle cx="233" cy="67" r="32"/>
      <circle cx="43" cy="202" r="32"/><circle cx="233" cy="202" r="32"/>
    </g>
    <g fill="var(--red)">
      <path d="M30 70 l4-9 h18 l4 9 h3 v8 h-32 v-8z"/><circle cx="35" cy="79" r="3"/><circle cx="51" cy="79" r="3"/>
      <rect x="225" y="54" width="16" height="26" rx="3"/>
      <rect x="29" y="192" width="0" height="0"/>
      <path d="M218 193 h30 v20 h-30z"/>
    </g>
    <path d="M218 194 l15 11 l15-11" fill="none" stroke="var(--white)" stroke-width="2"/>
    <rect x="228" y="58" width="10" height="16" fill="var(--white)"/>
    <text x="43" y="213" text-anchor="middle" font-size="30" font-weight="700" fill="var(--red)" font-family="Montserrat,sans-serif">$</text>
    <text x="138" y="128" text-anchor="middle" font-size="14" font-weight="600" fill="var(--dark)" font-family="Montserrat,sans-serif" letter-spacing="2">KELMORVA</text>
    <text x="138" y="146" text-anchor="middle" font-size="10" font-weight="600" fill="var(--dark)" font-family="Montserrat,sans-serif" letter-spacing="2">MARKETING</text>
  </svg>
  <footer class="footer"><span class="copy">© 2024 Kelmorva Marketing. All Rights Reserved.</span><span class="bar"></span><span class="red"></span><span class="page">Page &nbsp;| 01</span></footer>
</section>

<!-- Slide 02 -->
<section class="slide" style="left:433px;top:54px">
  <div class="rule"></div>
  <h1 class="title">Trade-In-Leads-Valuation Flow</h1>
  <p class="subtitle">Trade-In Leads: Offering Credit Pre-Qualification</p>
  <div class="brand">KELMORVA<br>MARKETING</div>
  <svg class="abs" style="left:40px;top:124px" width="230" height="230" viewBox="0 0 230 230">
    <path d="M115 3 A112 112 0 0 1 115 227" fill="none" stroke="var(--red)" stroke-width="6"/>
    <path d="M115 227 A112 112 0 0 1 115 3" fill="none" stroke="var(--dark)" stroke-width="6"/>
    <defs><linearGradient id="ph1" x1="0" y1="0" x2="1" y2="1"><stop offset="0" stop-color="#d9d4cc"/><stop offset="1" stop-color="#8a8f9a"/></linearGradient></defs>
    <circle cx="115" cy="115" r="105" fill="url(#ph1)" role="img" aria-label="Photo of hands holding a smartphone showing a trade-in text conversation"/>
  </svg>
  <div class="abs" style="left:43px;top:169px;width:72px;height:42px;background:var(--white);border:2px solid var(--dark);border-radius:8px;font-size:8px;font-weight:600;display:flex;align-items:center;justify-content:center">PRE-QUALIFIED</div>
  <svg class="abs" style="left:320px;top:172px" width="350" height="92" viewBox="0 0 350 92">
    <g fill="var(--white)" style="filter:drop-shadow(0 2px 4px rgba(0,0,0,.18))">
      <circle cx="45" cy="45" r="42"/><circle cx="177" cy="45" r="42"/><circle cx="307" cy="45" r="42"/>
    </g>
    <g fill="var(--red)"><circle cx="101" cy="45" r="3"/><circle cx="110" cy="45" r="3"/><circle cx="119" cy="45" r="3"/>
      <circle cx="232" cy="45" r="3"/><circle cx="241" cy="45" r="3"/><circle cx="250" cy="45" r="3"/></g>
    <path d="M35 30 h14 l-4 6 q14 6 12 22 h-28 q-2-16 12-22z" fill="var(--dark)"/>
    <circle cx="55" cy="58" r="9" fill="var(--dark)" stroke="var(--white)" stroke-width="2"/>
    <path d="M51 58 l3 3 l5-6" fill="none" stroke="var(--white)" stroke-width="2"/>
    <g fill="var(--red)"><rect x="160" y="46" width="6" height="16"/><rect x="169" y="40" width="6" height="22"/><rect x="178" y="48" width="6" height="14"/><rect x="187" y="38" width="6" height="24"/></g>
    <path d="M160 38 l10-8 l8 6 l14-10" fill="none" stroke="var(--red)" stroke-width="2.5"/>
    <circle cx="305" cy="47" r="14" fill="none" stroke="var(--dark)" stroke-width="4"/>
    <text x="305" y="53" text-anchor="middle" font-size="15" font-weight="700" fill="var(--dark)" font-family="Montserrat,sans-serif">$</text>
    <path d="M318 30 a20 20 0 0 1 6 12" fill="none" stroke="var(--dark)" stroke-width="4"/>
  </svg>
  <p class="label" style="left:310px;top:267px;width:110px">Customer texts<br>for vehicle value</p>
  <p class="label" style="left:442px;top:267px;width:110px">Receives trade-in<br>appraisal</p>
  <p class="label" style="left:567px;top:267px;width:120px">Offer to pre-qualify<br>for financing</p>
  <footer class="footer"><span class="copy">© 2024 Kelmorva Marketing. All Rights Reserved.</span><span class="bar"></span><span class="red"></span><span class="page">Page &nbsp;| 02</span></footer>
</section>

<!-- Slide 03 -->
<section class="slide" style="left:821px;top:54px">
  <div class="rule"></div>
  <h1 class="title">Credit Leads - Pre-Qualified Flow</h1>
  <p class="subtitle">Pre-Qualified Leads: Offering Trade-In Appraisal</p>
  <div class="brand">KELMORVA<br>MARKETING</div>
  <svg class="abs" style="left:37px;top:124px" width="230" height="230" viewBox="0 0 230 230">
    <path d="M115 3 A112 112 0 0 1 115 227" fill="none" stroke="var(--red)" stroke-width="6"/>
    <path d="M115 227 A112 112 0 0 1 115 3" fill="none" stroke="var(--dark)" stroke-width="6"/>
    <defs><linearGradient id="ph2" x1="0" y1="0" x2="1" y2="1"><stop offset="0" stop-color="#e9e6e6"/><stop offset="1" stop-color="#b8a9a4"/></linearGradient></defs>
    <circle cx="115" cy="115" r="105" fill="url(#ph2)" role="img" aria-label="Photo of a laptop showing a pre-qualification congratulations email"/>
  </svg>
  <div class="abs" style="left:40px;top:168px;width:72px;height:42px;background:var(--white);border:2px solid var(--dark);border-radius:8px;font-size:8px;font-weight:600;display:flex;align-items:center;justify-content:center;text-align:center;line-height:1.2">PRE-QUALIFY<br>FOR FINANCING</div>
  <svg class="abs" style="left:320px;top:167px" width="360" height="92" viewBox="0 0 360 92">
    <g fill="var(--white)" style="filter:drop-shadow(0 2px 4px rgba(0,0,0,.18))">
      <circle cx="46" cy="45" r="42"/><circle cx="182" cy="45" r="42"/><circle cx="314" cy="45" r="42"/>
    </g>
    <g fill="var(--red)"><circle cx="103" cy="45" r="3"/><circle cx="112" cy="45" r="3"/><circle cx="121" cy="45" r="3"/>
      <circle cx="239" cy="45" r="3"/><circle cx="248" cy="45" r="3"/><circle cx="257" cy="45" r="3"/></g>
    <g fill="var(--red)"><circle cx="46" cy="31" r="7"/><circle cx="31" cy="36" r="5.5"/><circle cx="61" cy="36" r="5.5"/>
      <path d="M35 58 v-10 a11 11 0 0 1 22 0 v10z"/><path d="M22 58 v-8 a9 9 0 0 1 11-8 v16z"/><path d="M70 58 v-8 a9 9 0 0 0-11-8 v16z"/></g>
    <path d="M160 56 a22 22 0 0 1 44 0" fill="none" stroke="var(--dark)" stroke-width="9" stroke-dasharray="10 3"/>
    <path d="M182 56 l-6-14 l10 12z" fill="var(--dark)"/>
    <path d="M294 48 l40-20 l-14 36 l-8-12z" fill="var(--red)"/>
    <path d="M312 52 l22-24" stroke="var(--white)" stroke-width="2"/>
  </svg>
  <p class="label" style="left:311px;top:263px;width:110px">Customer<br>pre-qualifies via<br>Swift4Loan</p>
  <p class="label" style="left:447px;top:263px;width:110px">Receives credit<br>approval</p>
  <p class="label" style="left:579px;top:263px;width:110px">Email and Mail</p>
  <footer class="footer"><span class="copy">© 2024 Kelmorva Marketing. All Rights Reserved.</span><span class="bar"></span><span class="red"></span><span class="page">Page &nbsp;| 03</span></footer>
</section>

<!-- Slide 04 -->
<section class="slide" style="left:45px;top:286px">
  <div class="rule"></div>
  <h1 class="title">Multiple Lead Sources Feeding Into<br>The Program</h1>
  <div class="brand">KELMORVA<br>MARKETING</div>
  <svg class="abs" style="left:230px;top:124px" width="290" height="240" viewBox="0 0 290 240">
    <path d="M4 2 h264 q8 0 4 8 l-44 76 h-182z" fill="var(--red)"/>
    <path d="M40 98 h216 l-96 138 q-6 6-12 0z" fill="var(--dark)"/>
    <circle cx="135" cy="44" r="28" fill="none" stroke="var(--white)" stroke-width="2"/>
    <path d="M125 56 l14-14 m2-2 a6 6 0 1 1 5-5" fill="none" stroke="var(--white)" stroke-width="4" stroke-linecap="round"/>
    <circle cx="135" cy="148" r="28" fill="none" stroke="var(--white)" stroke-width="2"/>
    <rect x="123" y="140" width="24" height="16" rx="2" fill="var(--white)"/>
    <path d="M123 141 l12 9 l12-9" fill="none" stroke="var(--dark)" stroke-width="2"/>
  </svg>
  <div class="abs" style="left:35px;top:155px;width:228px;height:40px;background:var(--red);border-radius:20px;color:var(--white);font-size:11px;text-align:right;padding:5px 30px 0 0;line-height:1.45">Pre-Qualification Tool<br>(Swift4Loan)- How it Works</div>
  <p class="abs" style="left:40px;top:208px;width:187px;text-align:right;font-size:11px;color:var(--ink);line-height:1.45">Converts Web Traffic into the<br>highest quality lead on the</p>
  <div class="abs" style="left:443px;top:237px;width:220px;height:40px;background:var(--dark);border-radius:20px;color:var(--white);font-size:11px;padding:5px 0 0 22px;line-height:1.45">Replyon Email/Mail Marketing<br>How it Works</div>
  <p class="abs" style="left:450px;top:285px;font-size:10px;color:var(--ink);line-height:1.5">Delivers actionable leads from email<br>marketing not Just OPENS AND CLICKS.</p>
  <ol class="abs tiny" style="left:450px;top:322px;list-style:none;line-height:1.75;font-size:7px">
    <li><span style="color:var(--red)">1.)</span> Past Sold Customers (Equity Targets)</li>
    <li><span style="color:var(--red)">2.)</span> Past Service Onlu Department Customers (Conquest Sales)</li>
    <li><span style="color:var(--red)">3.)</span> Unsold Leads (from previous interactions)</li>
  </ol>
  <footer class="footer"><span class="copy">© 2024 Kelmorva Marketing. All Rights Reserved.</span><span class="bar"></span><span class="red"></span><span class="page">Page &nbsp;| 04</span></footer>
</section>

<!-- Slide 05 -->
<section class="slide" style="left:433px;top:286px">
  <div class="rule"></div>
  <h1 class="title">Cross-Offer Opportunities</h1>
  <div class="brand">KELMORVA<br>MARKETING</div>
  <div class="card" style="left:38px">
    <h3><em>Cross-Offer Opportunities for</em><br>Maximum Engagement</h3>
    <p class="tiny" style="margin-top:38px;font-size:9px">Offer Trade-In Valuation</p>
    <svg width="194" height="90" viewBox="0 0 194 90">
      <path d="M97 6 v18 m-4-14 l4-5 l4 5 m-4 10 l0 0" fill="none" stroke="var(--dark)" stroke-width="1.5"/>
      <path d="M93 20 l4 5 l4-5" fill="none" stroke="var(--dark)" stroke-width="1.5"/>
      <ellipse cx="97" cy="44" rx="34" ry="14" fill="none" stroke="var(--red)" stroke-width="1.3"/>
      <text x="97" y="48" text-anchor="middle" font-size="10" fill="var(--red)" font-family="Montserrat,sans-serif">Start as a Credit Lead</text>
      <path d="M97 62 v20 m-4-16 l4-5 l4 5 m-8 11 l4 5 l4-5" fill="none" stroke="var(--dark)" stroke-width="1.5"/>
    </svg>
    <p class="tiny" style="font-size:9px">Offer Credit Pre-Qualification</p>
  </div>
  <div class="card" style="left:261px">
    <h3><em>Engage To Convert One Lead<br>Type To Get Both With</em><br>Email/mail &amp; Digital Retargeting</h3>
    <svg style="margin-top:14px" width="194" height="120" viewBox="0 0 194 120">
      <circle cx="98" cy="58" r="46" fill="none" stroke="var(--red)" stroke-width="1" stroke-dasharray="3 3"/>
      <circle cx="110" cy="16" r="11" fill="var(--red)"/>
      <rect x="104" y="12" width="12" height="8" fill="var(--white)"/>
      <circle cx="52" cy="58" r="11" fill="var(--dark)"/>
      <rect x="47" y="53" width="10" height="10" rx="3" fill="none" stroke="var(--white)" stroke-width="1.3"/>
      <circle cx="134" cy="90" r="11" fill="var(--dark)"/>
      <circle cx="134" cy="90" r="4" fill="var(--white)"/>
      <circle cx="98" cy="52" r="9" fill="none" stroke="var(--red)" stroke-width="1.8"/>
      <path d="M82 80 a16 14 0 0 1 32 0z" fill="none" stroke="var(--red)" stroke-width="1.8"/>
    </svg>
  </div>
  <div class="card" style="left:484px">
    <h3><em>Leverage Email &amp; Social<br>Retargeting</em> to Drive<br>Cross-Action</h3>
    <svg style="margin-top:4px" width="194" height="140" viewBox="0 0 194 140">
      <rect x="61" y="6" width="10" height="7" fill="var(--red)"/>
      <circle cx="97" cy="10" r="4" fill="var(--red)"/>
      <rect x="123" y="6" width="8" height="8" rx="2" fill="none" stroke="var(--red)" stroke-width="1.3"/>
      <circle cx="97" cy="84" r="46" fill="none" stroke="var(--red)" stroke-width="1" stroke-dasharray="3 3"/>
      <circle cx="61" cy="60" r="9" fill="var(--red)"/><circle cx="134" cy="60" r="9" fill="var(--red)"/>
      <circle cx="72" cy="119" r="9" fill="var(--dark)"/><circle cx="128" cy="119" r="9" fill="var(--dark)"/>
      <g font-family="Montserrat,sans-serif" font-size="7.5" fill="var(--ink)">
        <text x="30" y="55">Credit</text><text x="34" y="64">lead</text>
        <text x="150" y="55">Trade-in</text><text x="150" y="64">offer</text>
        <text x="44" y="112">Pre</text><text x="16" y="121">qualification</text>
        <text x="145" y="115">Trade-in</text><text x="145" y="124">lead</text>
      </g>
    </svg>
  </div>
  <p class="abs" style="left:0;top:348px;width:720px;text-align:center;font-size:12.5px;font-weight:500;color:var(--ink)">Stay Top Of Mind &amp; Convert Leads Into Multi-Action Customers</p>
  <footer class="footer"><span class="copy">© 2024 Kelmorva Marketing. All Rights Reserved.</span><span class="bar"></span><span class="red"></span><span class="page">Page &nbsp;| 05</span></footer>
</section>

<!-- Slide 06 -->
<section class="slide" style="left:821px;top:286px">
  <div class="rule"></div>
  <h1 class="title">Lead Conversion Goals</h1>
  <p class="subtitle">Converting Leads into Sales</p>
  <div class="brand">KELMORVA<br>MARKETING</div>
  <div class="photo" role="img" aria-label="Photo of a smiling customer in a new car receiving the keys" style="left:38px;top:126px;width:301px;height:222px;background:linear-gradient(135deg,#3c3c3e,#8d8a86 55%,#c9c3bb);border-bottom:3px solid var(--red)"></div>
  <svg class="abs" style="left:390px;top:105px" width="300" height="260" viewBox="0 0 300 260">
    <g fill="none" stroke="var(--soft)" stroke-width="5">
      <circle cx="62" cy="60" r="54"/><circle cx="232" cy="60" r="54"/><circle cx="62" cy="194" r="54"/><circle cx="232" cy="194" r="54"/>
    </g>
    <g fill="none" stroke="var(--red)" stroke-width="5">
      <path d="M62 6 A54 54 0 0 0 8 60"/><path d="M232 6 A54 54 0 0 1 286 60"/>
      <path d="M8 194 A54 54 0 0 1 62 140"/><path d="M232 140 A54 54 0 0 1 286 194"/>
    </g>
    <circle cx="62" cy="60" r="42" fill="var(--red)"/><circle cx="232" cy="60" r="42" fill="var(--dark)"/>
    <circle cx="62" cy="194" r="42" fill="var(--dark)"/><circle cx="232" cy="194" r="42" fill="var(--red)"/>
    <g font-family="Montserrat,sans-serif" font-weight="700" fill="var(--white)" text-anchor="middle">
      <text x="62" y="67" font-size="28">75%</text><text x="232" y="67" font-size="28">9.35</text>
      <text x="62" y="201" font-size="28">12</text><text x="232" y="201" font-size="28">35</text>
    </g>
    <g font-family="Montserrat,sans-serif" font-size="6" fill="var(--white)" text-anchor="middle">
      <text x="62" y="80">Maecenas vel tortor</text><text x="232" y="80">Aliquam erat volutpat</text>
      <text x="62" y="214">Proin dolor</text><text x="232" y="214">Curabitur venenatis</text>
    </g>
  </svg>
  <footer class="footer"><span class="copy">© 2024 Kelmorva Marketing. All Rights Reserved.</span><span class="bar"></span><span class="red"></span><span class="page">Page &nbsp;| 06</span></footer>
</section>

</main>
</body>
</html>
```